Water Filter Company Needs Bizz Cards!!

Need business cards for my company. We sell whole home water filters and salt free water softeners. No more buying bottled water. Our filtering units filter out all heavy metals, chlorine, and VOC's, last 15 years, and are maintenance free and supply your whole home with spring quality alkaline water. Our Salt free water conditioners, eliminate hard water and scale, without lowering the ph, or TDS's (total Dissolved solids)

I think this is the color code we are using on my site. My logo looks good behind it. #192841

Website will be www.Brovexa.com

Industry/Entity Type

Water Purification

Contact Information for Business Card

For now, just insert standard Dummy text. I need these text lines for the info to be editable so i can make them for multiple employees. I do have Photoshop and illustrator, unless there is a simpler program i can use solely for biz cards

Font styles to use
Sans Serif

Requirements
Must have
• Use my preexisting logo.

www.BroVexa.com

Spring Quality Alkaline Water at every tap.

List out services. Whole Home Water Filters, Salt Free Water Softeners, Clarimont KT7, UV Sterilizers
Nice to have
• I think this is the color code we are using on my site. My logo looks good behind it. #192841 or black. Please no white or light blue backgrounds.

Maybe a picture of my tank.

Slogan like Spring Quality Alkaline Water at every tap.
And just list the services Whole Home Water Filters, Salt Free Water Softeners, Clarimont KT7, UV Sterilizers

I think I would like to not have a contrasting textured logo like I see on some of them. I may use it for my personal cards, but new employees may not want the extra expense.
Should not have
• A different logo than the one provided.

White or baby blue backgrounds. Use the color code, or blacks.

```html
<!DOCTYPE html>
<html lang="en">
<head>
<meta charset="utf-8">
<title>Brovexa Business Card</title>
<link href="https://fonts.googleapis.com/css2?family=Josefin+Sans:wght@300;400;600;700&display=swap" rel="stylesheet">
<style>
  :root{
    --page:#e9e9e9;
    --navy:#16223b;
    --blue:#1d8fd0;
    --sky:#45b0e0;
    --deep:#0a7cc4;
    --grey:#c6c8ca;
    --text:#d9dde3;
    --white:#ffffff;
  }
  *{margin:0;padding:0;box-sizing:border-box}
  html,body{width:1200px;height:1200px;overflow:hidden}
  body{background:var(--page);font-family:"Josefin Sans",sans-serif;position:relative}
  .card{position:absolute;left:227px;width:746px;height:425px;background:var(--navy);border-radius:37px;overflow:hidden}
  .card--front{top:135px}
  .card--back{top:638px}

  .splash{position:absolute;left:0;top:0;width:150px;height:425px}
  .product-tank{position:absolute;left:627px;top:27px;width:76px;height:372px;border-radius:8px 8px 12px 12px;
    background:linear-gradient(90deg,#0c0c0e 0%,#2a2b2f 45%,#111114 100%)}
  .tagline-band{position:absolute;left:130px;top:358px;width:495px;height:40px;
    background:linear-gradient(90deg,var(--sky),var(--deep))}
  .tagline-band__end{position:absolute;left:708px;top:358px;width:38px;height:40px;background:var(--grey)}
  .tagline{position:absolute;left:186px;top:369px;color:var(--white);font-size:18px;font-weight:300;letter-spacing:.3px;white-space:nowrap}

  .brand{position:absolute;display:flex;align-items:center;gap:14px}
  .brand__dot{border-radius:50%;background:var(--sky)}
  .brand__name{color:var(--sky);font-weight:700;letter-spacing:-1px;line-height:1}
  .card--front .brand{left:110px;top:40px}
  .card--front .brand__dot{width:44px;height:44px}
  .card--front .brand__name{font-size:76px}
  .card--back .brand{left:50px;top:178px}
  .card--back .brand__dot{width:40px;height:40px}
  .card--back .brand__name{font-size:70px}

  .person{position:absolute;left:188px;top:178px}
  .person__name{color:var(--blue);font-size:26px;font-weight:400}
  .person__role{color:var(--text);font-size:18px;font-weight:300;margin-top:4px}

  .contacts{position:absolute;left:188px;top:263px;list-style:none}
  .contacts li{display:flex;align-items:center;gap:11px;height:25.5px;color:var(--text);font-size:18px;font-weight:300}
  .contacts svg{width:18px;height:18px;flex:none}

  .address{position:absolute;left:411px;top:285px;color:var(--text);font-size:18px;font-weight:300;line-height:25px;font-style:normal}

  .services{position:absolute;left:477px;top:172px;list-style:none}
  .services li{display:flex;align-items:center;gap:9px;height:22px;color:var(--text);font-size:17px;font-weight:300;letter-spacing:.4px}
  .services svg{width:12px;height:15px;flex:none}
</style>
</head>
<body>

<section class="card card--front">
  <svg class="splash" viewBox="0 0 150 425" role="img" aria-label="Splashing water with bubbles">
    <defs>
      <linearGradient id="splashFill" x1="0" y1="0" x2="1" y2="1">
        <stop offset="0" stop-color="#3fa0dc"/>
        <stop offset=".6" stop-color="#1a86cf"/>
        <stop offset="1" stop-color="#0b6fb8"/>
      </linearGradient>
    </defs>
    <path d="M0 0 H83 C70 70 75 160 100 240 C120 300 140 360 120 425 H0 Z" fill="url(#splashFill)"/>
  </svg>

  <div class="brand">
    <span class="brand__dot"></span>
    <span class="brand__name">Brovexa</span>
  </div>

  <div class="person">
    <p class="person__name">Daniel Harwood</p>
    <p class="person__role">Managing Director</p>
  </div>

  <ul class="contacts">
    <li>
      <svg viewBox="0 0 18 18"><circle cx="9" cy="9" r="9" fill="var(--blue)"/><path d="M4.5 7.5c0-2 9-2 9 0v1h-2.5v-1h-4v1H4.5z M6 9h6l1.5 4h-9z" fill="var(--navy)"/></svg>
      (84) 0987 654 321
    </li>
    <li>
      <svg viewBox="0 0 18 18"><circle cx="9" cy="9" r="9" fill="var(--blue)"/><rect x="4.5" y="5.5" width="9" height="7" rx="1" fill="none" stroke="var(--navy)" stroke-width="1.3"/><path d="M4.8 6l4.2 3.5L13.2 6" fill="none" stroke="var(--navy)" stroke-width="1.3"/></svg>
      info@brovexa.com
    </li>
    <li>
      <svg viewBox="0 0 18 18"><circle cx="9" cy="9" r="9" fill="var(--blue)"/><circle cx="9" cy="9" r="5" fill="none" stroke="var(--navy)" stroke-width="1.3"/><path d="M4 9h10M9 4v10" stroke="var(--navy)" stroke-width="1"/></svg>
      www.brovexa.com
    </li>
  </ul>

  <address class="address">2450 Harbor Lane,<br>Washington DC, USA</address>

  <div class="tagline-band"></div>
  <div class="tagline-band__end"></div>
  <p class="tagline">Spring Quality Alkaline Water at every tap</p>

  <div class="product-tank" role="img" aria-label="Photo of the whole home water filter tank"></div>
</section>

<section class="card card--back">
  <div class="brand">
    <span class="brand__dot"></span>
    <span class="brand__name">Brovexa</span>
  </div>

  <ul class="services">
    <li><svg viewBox="0 0 12 15"><path d="M6 0C4 4 0 7 0 10a6 5 0 0 0 12 0C12 7 8 4 6 0z" fill="var(--sky)"/></svg>Whole home water filters</li>
    <li><svg viewBox="0 0 12 15"><path d="M6 0C4 4 0 7 0 10a6 5 0 0 0 12 0C12 7 8 4 6 0z" fill="var(--sky)"/></svg>Salt free water softeners</li>
    <li><svg viewBox="0 0 12 15"><path d="M6 0C4 4 0 7 0 10a6 5 0 0 0 12 0C12 7 8 4 6 0z" fill="var(--sky)"/></svg>Clarimont KT7</li>
    <li><svg viewBox="0 0 12 15"><path d="M6 0C4 4 0 7 0 10a6 5 0 0 0 12 0C12 7 8 4 6 0z" fill="var(--sky)"/></svg>UV Sterilizers</li>
  </ul>
</section>

</body>
</html>
```